Flyer Design Project

I require a double sided flyer in PSD format.
The flyer should look fresh and clean.
The flyer is for an digital marketing company that offers various services. The services are broken down into 3 main categories and the design should reflect this.
All the content is provided in the attached file
Industry/Entity Type
Digital
Requirements
Must have
- Front of the leaflet to be mainly white background with appealing text based questions in the colours in large font with relevant images.
Back if the
3 separate boxes using the colours indicated in the attachment for the services on back of the leafet.
Should not have
- Gradients
Borders on the edges of the design
Vignettes
Black elements
Any text below 10pt
Fancy fonts
Do not use old-style fonts

```html
<!DOCTYPE html>
<html lang="en">
<head>
<meta charset="utf-8">
<title>Brightlane Flyer – Front and Back</title>
<link rel="stylesheet" href="https://fonts.googleapis.com/css2?family=Righteous&family=Arimo:wght@400;700&display=swap">
<style>
:root{
  --stage:#1b1b1b;
  --paper:#ffffff;
  --lime:#b5d334;
  --lime-dark:#1f9a3c;
  --sky:#2fc1ef;
  --sky-dark:#1577c3;
  --amber:#fbbf4a;
  --orange:#f7993a;
  --orange-dark:#ef6a23;
  --navy:#1e3a78;
  --grey:#9d9d9f;
  --grey-text:#7a7a7c;
  --blue-text:#1a6fbf;
  --white:#ffffff;
}
*{box-sizing:border-box;margin:0;padding:0}
html,body{width:1200px;height:736px;overflow:hidden}
body{background:var(--stage);position:relative;font-family:"Arimo",Arial,sans-serif}
.display{font-family:"Righteous","Arial Black",sans-serif;text-transform:uppercase;line-height:1}

/* ---------- Front ---------- */
.flyer-front{position:absolute;left:92px;top:70px;width:428px;height:590px;background:var(--paper);overflow:hidden}
.band{position:absolute;left:0;width:100%}
.band-lime{top:18px;height:112px;background:var(--lime);clip-path:polygon(0 14%,100% 0,100% 80%,0 100%)}
.band-sky{top:120px;height:62px;background:var(--sky);clip-path:polygon(0 12%,100% 0,100% 78%,0 100%)}
.band-amber{top:162px;height:100px;background:var(--amber);clip-path:polygon(0 22%,100% 0,100% 82%,0 100%)}
.question{position:absolute;color:var(--white);transform:rotate(-3.5deg);transform-origin:left top}
.question small{display:block;font-size:8px;letter-spacing:.5px}
.q-consumers{left:72px;top:46px}
.q-consumers .big{font-size:25px}
.q-consumers .mid{font-size:15px;margin-left:42px}
.q-consumers small.indent{margin-left:118px}
.q-online{left:38px;top:134px}
.q-online .big{font-size:19px}
.q-more{right:30px;top:180px;text-align:right;transform-origin:right top}
.q-more .big{font-size:27px}
.q-more .mid{font-size:13px}
.hero-art{position:absolute;left:90px;top:262px;width:250px;height:220px;background:radial-gradient(ellipse at 50% 60%,#dfe8f5 0%,#f3f6fb 60%,#ffffff 100%)}
.tagline{position:absolute;right:152px;top:478px;text-align:right;font-size:14px;color:var(--grey-text)}
.brand-disc{position:absolute;border-radius:50%;background:var(--grey);color:var(--white);display:flex;align-items:center;justify-content:center;font-family:"Righteous","Arial Black",sans-serif}
.flyer-front .brand-disc{left:296px;top:440px;width:96px;height:96px;font-size:15px}
.call-bar{position:absolute;background:var(--grey);color:var(--white);font-weight:700;text-align:center}
.flyer-front .call-bar{left:30px;right:6px;top:548px;height:26px;font-size:15px;line-height:26px}

/* ---------- Back ---------- */
.flyer-back{position:absolute;left:550px;top:146px;width:610px;height:455px;background:var(--paper);overflow:hidden}
.service{position:absolute;top:30px;height:300px;color:var(--white);padding:14px 10px 0}
.service-consulting{left:28px;width:178px;background:var(--lime)}
.service-design{left:212px;width:160px;background:var(--sky)}
.service-sem{left:394px;width:176px;background:var(--orange)}
.service h2{text-align:center;font-weight:400}
.service h2 .main{display:block;font-size:25px;white-space:nowrap}
.service h2 .sub{display:block;font-size:19px;margin-top:4px}
.service ul{list-style:none;margin-top:12px}
.service li{font-size:11px;line-height:13px;font-weight:700;position:relative;padding-left:16px;margin-bottom:13px}
.service-design li{white-space:nowrap}
.service-sem li{margin-bottom:2px;font-size:10.5px;white-space:nowrap}
.service li::before{content:"";position:absolute;left:0;top:1px;width:10px;height:10px;background:var(--white)}
.service li::after{content:"";position:absolute;left:3px;top:2px;width:3px;height:6px;border:solid var(--lime-dark);border-width:0 2px 2px 0;transform:rotate(45deg)}
.coupon{position:absolute;left:14px;right:14px;bottom:12px;height:84px;border:2px dashed var(--navy);text-align:center;font-weight:700;color:var(--white);white-space:nowrap}
.coupon .big{display:block;font-size:42px;line-height:1;margin-top:6px}
.coupon .small{display:block;font-size:17px;margin-top:2px}
.service-consulting .coupon{background:var(--lime-dark)}
.service-design .coupon{background:var(--sky-dark)}
.service-sem .coupon{background:var(--orange-dark)}
.service-sem .coupon .big{font-size:32px;margin-top:12px}
.service-sem .coupon .small{font-size:15px;margin-top:4px}
.scissors{position:absolute;right:2px;top:-12px;width:14px;height:12px}
.flyer-back .brand-disc{left:74px;top:372px;width:54px;height:54px;font-size:9px}
.divider{position:absolute;left:162px;top:368px;width:1px;height:60px;background:var(--blue-text)}
.address{position:absolute;left:190px;top:364px;color:var(--blue-text);font-size:12px;line-height:14px;font-style:normal}
.address strong{font-size:15px;display:block;margin-bottom:2px}
.flyer-back .call-bar{left:300px;top:346px;width:270px;height:64px;padding-top:10px}
.call-bar .phone{display:block;font-size:22px}
.call-bar .note{display:block;font-size:14px;margin-top:2px}
</style>
</head>
<body>

<section class="flyer-front" aria-label="Flyer front">
  <div class="band band-lime"></div>
  <div class="band band-sky"></div>
  <div class="band band-amber"></div>

  <p class="question q-consumers display">
    <small>Did you know</small>
    <span class="big">85% of consumers</span>
    <small class="indent">Use the internet</small>
    <span class="mid">To find businesses like yours?</span>
  </p>
  <p class="question q-online display">
    <small>Are your</small>
    <span class="big">Customers finding you online?</span>
  </p>
  <p class="question q-more display">
    <small>Do you need</small>
    <span class="big">More customers</span><br>
    <span class="mid">For your business?</span>
  </p>

  <div class="hero-art" role="img" aria-label="Illustration of figures with a laptop and envelope beside large blue WWW letters"></div>

  <p class="tagline display">Let us help you<br>grow your business online</p>
  <div class="brand-disc">Brightlane</div>
  <div class="call-bar">Call 0121 555 0148 for a FREE consultation</div>
</section>

<section class="flyer-back" aria-label="Flyer back">
  <article class="service service-consulting">
    <h2 class="display"><span class="main">Consulting</span><span class="sub">Services</span></h2>
    <ul>
      <li>Marketing Strategy And Planning</li>
      <li>Business Branding</li>
      <li>Competition Analysis</li>
    </ul>
    <div class="coupon">
      <svg class="scissors" viewBox="0 0 14 12"><circle cx="3" cy="9" r="2" fill="none" stroke="#fff" stroke-width="1.2"/><circle cx="11" cy="9" r="2" fill="none" stroke="#fff" stroke-width="1.2"/><path d="M4 7.5 10 1M10 7.5 4 1" stroke="#fff" stroke-width="1.2"/></svg>
      <span class="big">FREE</span><span class="small">Consultation</span>
    </div>
  </article>

  <article class="service service-design">
    <h2 class="display"><span class="main">Design</span><span class="sub">Services</span></h2>
    <ul>
      <li>Web Design</li>
      <li>Website Maintenance</li>
      <li>Logo Design</li>
      <li>Flyer Design</li>
    </ul>
    <div class="coupon">
      <svg class="scissors" viewBox="0 0 14 12"><circle cx="3" cy="9" r="2" fill="none" stroke="#fff" stroke-width="1.2"/><circle cx="11" cy="9" r="2" fill="none" stroke="#fff" stroke-width="1.2"/><path d="M4 7.5 10 1M10 7.5 4 1" stroke="#fff" stroke-width="1.2"/></svg>
      <span class="big">FREE</span><span class="small">Website</span>
    </div>
  </article>

  <article class="service service-sem">
    <h2 class="display"><span class="main">SEM</span><span class="sub">Services</span></h2>
    <ul>
      <li>Local Business Marketing</li>
      <li>Ppc</li>
      <li>Email Marketing</li>
      <li>Seo</li>
      <li>Social Media</li>
      <li>Content Development</li>
      <li>Website Audit</li>
      <li>Lead Generation</li>
    </ul>
    <div class="coupon">
      <svg class="scissors" viewBox="0 0 14 12"><circle cx="3" cy="9" r="2" fill="none" stroke="#fff" stroke-width="1.2"/><circle cx="11" cy="9" r="2" fill="none" stroke="#fff" stroke-width="1.2"/><path d="M4 7.5 10 1M10 7.5 4 1" stroke="#fff" stroke-width="1.2"/></svg>
      <span class="big">25% OFF</span><span class="small">any SEM Package</span>
    </div>
  </article>

  <div class="brand-disc">Brightlane</div>
  <div class="divider"></div>
  <address class="address"><strong>Brightlane</strong>12 Canal Walk<br>Birmingham<br>B1 4QT</address>
  <div class="call-bar"><span class="phone">Call 0121 555 0100</span><span class="note">for a FREE consultation</span></div>
</section>

</body>
</html>
```